KLD Photography Editing & Support Services for Real Estate

We require a double sided A4 flyer to promote our photography services to real estate agencies.
This particular service is targeted to rural areas where reliable, professional and highly skilled photographers are difficult to source. We teach the agent how to photograph, they upload files to a server and we take care of the rest (image editing, quality control and delivery). This will give the agents flexibility with when to shoot and eliminates the stress of managing a photographer / contractor. We offer a 1 day face to face training session and competitive packages for equipment start up.
We would like the flyer to look clean & very professional. The flyer should showcase samples of our work to highlight what can be achieved by using our services. We like the look of a black or dark background behind the text and feel that would look nice with our photographs provided. Otherwise open to your suggestions and ideas.
TEXT FOR FLYER:
Welcome to the KLD Real Estate Photography Editing and Support Service
• Take your real estate business to the next level by providing impressive real estate imagery that makes you stands out from the competition
• Omit the stress of trying to find a good photographer or managing an unreliable one and hence have more time to focus on other aspects of your business
• Showcase your listings with better quality and more impactful photographs than your competitors thereby increasing potential for a quick sale
• Great first impressions matter and you will achieve this by looking and feeling more professional. This will attract and retain more future clients.
HOW IT WORKS
• We understand that your time is valuable, so let us handle the editing and delivery of your images. You shoot, and we take care of the rest.
• Images are edited and delivered within 1 working day
INCLUSIONS:
• Full day face to face training (we come to you) and instructional handbook
• We will teach you everything you need to know about your equipment and how to take stunning real estate photographs
• Service turnaround within 1 working day
• Free HELP desk service Mon-Fri
• 12 month Exclusivity (rural towns only) for a limited time
INVESTMENT
• 99 per listing for us to manage images including editing, quality control and delivery (10 Images)
• Ask us about competitive packages for photography equipment if required
SUMMARY
The KLD Real Estate Photography Editing and Support Service is the perfect solution for busy real estate professionals who want to take their business to the next level. Our service is affordable, flexible, and designed to help you showcase your listings in the best possible light.
Contact us today to learn more about how we can help you.

```html
<!DOCTYPE html>
<html lang="en">
<head>
<meta charset="utf-8">
<title>KLD Real Estate Photography Flyer</title>
<link href="https://fonts.googleapis.com/css2?family=Archivo+Black&family=Arimo:wght@400&family=Great+Vibes&family=Montserrat:wght@300;400;500&display=swap" rel="stylesheet">
<style>
:root{
  --bg:#d8d6d7;
  --paper:#ffffff;
  --ink:#000000;
  --body:#5a5a5a;
  --rule:#333333;
  --silver-dark:#9a9a9c;
  --silver-light:#ffffff;
  --brand-grey:#8a8a8a;
}
*{box-sizing:border-box;margin:0;padding:0}
html,body{width:1200px;height:1200px;overflow:hidden;background:var(--bg)}
.page{
  position:absolute;top:222px;width:667px;height:945px;background:var(--paper);
  transform:scale(.8);transform-origin:0 0;overflow:hidden;
  box-shadow:0 2px 6px rgba(0,0,0,.25);
  font-family:"Arimo",Arial,sans-serif;color:var(--body);
}
.page--front{left:46px}
.page--back{left:621px}

/* brand name */
.brand{position:absolute;text-align:center;font-family:"Montserrat",sans-serif;font-weight:300;color:var(--brand-grey);text-transform:uppercase}
.page--front .brand{left:20px;top:70px;width:250px;font-size:19px;letter-spacing:5px;line-height:1.4}
.page--back .brand{right:40px;top:34px;width:150px;font-size:11px;letter-spacing:3px;line-height:1.4}

/* hero */
.hero{position:absolute;left:0;top:0;width:667px;height:350px}
.hero__photo{position:absolute;inset:0;background:linear-gradient(180deg,#8fb1d1 0%,#c9c3b8 32%,#3a3c40 55%,#4d5a3a 80%,#5c6b3e 100%)}
.hero__mask{position:absolute;left:0;top:0}

.title-box{
  position:absolute;left:45px;top:322px;width:576px;height:68px;background:var(--ink);
  border-radius:6px;text-align:center;color:#fff;
}
.title-box h1{
  font-family:"Archivo Black",sans-serif;font-weight:400;font-size:41px;line-height:1;margin-top:4px;
  background:linear-gradient(180deg,#ffffff 0%,#d9d9d9 45%,#8e8e8e 55%,#f2f2f2 100%);
  -webkit-background-clip:text;background-clip:text;color:transparent;letter-spacing:.5px;
}
.title-box p{font-family:"Montserrat",sans-serif;font-weight:500;font-size:15px;letter-spacing:.8px;margin-top:5px}

/* check lists */
.checks{list-style:none}
.checks li{position:relative;font-size:15.3px;line-height:19px;text-align:justify}
.checks li::before{content:"";position:absolute;left:-27px;top:3px;width:11px;height:11px;border:2px solid var(--ink)}
.checks li::after{content:"";position:absolute;left:-23px;top:1px;width:6px;height:11px;border:solid var(--ink);border-width:0 3px 3px 0;transform:rotate(40deg)}

.front-points{position:absolute;left:73px;top:414px;width:546px}
.front-points li{margin-bottom:14px}

.back-content{position:absolute;left:47px;top:55px;width:574px}
.back-content h2{font-family:"Archivo Black",sans-serif;font-weight:400;font-size:19px;color:var(--ink);letter-spacing:.5px;line-height:22px;border-bottom:1px solid var(--rule);padding-bottom:2px;width:572px}
.back-content .checks{margin:14px 0 12px 28px}
.back-content .checks li{margin-bottom:8px}

/* services band */
.band{position:absolute;left:0;top:640px;width:667px;height:95px;background:var(--ink)}
.band h3{font-family:"Archivo Black",sans-serif;font-weight:400;color:#f0f0f0;font-size:21px;text-align:center;margin-top:8px;letter-spacing:.6px}
.samples{position:absolute;left:35px;top:687px;display:flex;gap:10px}
.sample{width:192px;height:154px;border-radius:9px;border:2px solid #e3e3e3;box-shadow:0 0 0 1px #bdbdbd}

/* footer */
.footer{position:absolute;left:0;top:880px;width:667px;height:65px;background:linear-gradient(90deg,var(--silver-dark) 0%,#e6e6e6 25%,var(--silver-light) 50%,#e6e6e6 75%,var(--silver-dark) 100%)}
.footer p{font-family:"Montserrat",sans-serif;font-size:20px;color:#111;text-align:center;margin-top:24px}
.contact-pill{
  position:absolute;left:98px;top:856px;width:468px;height:42px;background:var(--ink);
  border:3px solid #fff;border-radius:22px;display:flex;align-items:center;justify-content:center;gap:12px;color:#fff;
}
.contact-pill .script{font-family:"Great Vibes",cursive;font-size:26px}
.contact-pill .phone{font-family:"Archivo Black",sans-serif;font-size:27px;letter-spacing:.5px;display:flex;align-items:center;gap:6px}
</style>
</head>
<body>

<section class="page page--front">
  <div class="hero">
    <div class="hero__photo" role="img" aria-label="Dark timber country house with lit porch and garden at dusk"></div>
    <svg class="hero__mask" width="667" height="130" viewBox="0 0 667 130">
      <path d="M0 0 H426 L300 92 Q262 118 220 120 H0 Z" fill="#fff"/>
    </svg>
  </div>
  <div class="brand">Marlo Kestrel<br><span style="font-size:11px;letter-spacing:4px">Photographer</span></div>

  <div class="title-box">
    <h1>WELCOME TO THE KLD</h1>
    <p>REAL ESTATE PHOTOGRAPHY EDITING AND SUPPORT SERVICE</p>
  </div>

  <ul class="checks front-points">
    <li>Take your real estate business to the next level by providing impressive real estate imagery that makes you stands out from the competition</li>
    <li>Omit the stress of trying to find a good photographer or managing an unreliable one and hence have more time to focus on other aspects of your business</li>
    <li>Showcase your listings with better quality and more impactful photographs than your competitors thereby increasing potential for a quick sale</li>
    <li>Great first impressions matter and you will achieve this by looking and feeling more professional. This will attract and retain more future clients.</li>
  </ul>

  <div class="band"><h3>PHOTOGRAPHY SERVICES</h3></div>
  <div class="samples">
    <div class="sample" role="img" aria-label="Timber living room with tall windows at dusk" style="background:linear-gradient(160deg,#8a6a48,#2c3a52 45%,#6b5a48)"></div>
    <div class="sample" role="img" aria-label="Bright hallway with framed artwork and timber floor" style="background:linear-gradient(160deg,#e8e4dc,#bca88a 55%,#5b4632)"></div>
    <div class="sample" role="img" aria-label="Dark sofa in a moody grey lounge" style="background:linear-gradient(160deg,#6d7076,#3b3d42 50%,#9a8a70)"></div>
  </div>

  <div class="footer"><p>www.marlokestrel.com | info@marlokestrel.com</p></div>
  <div class="contact-pill">
    <span class="script">Contact Us Today</span>
    <span class="phone">
      <svg width="24" height="24" viewBox="0 0 24 24"><circle cx="12" cy="12" r="12" fill="#fff"/><path d="M8 6c1 0 2 3 1.5 3.6L8.5 11c.9 2 2.5 3.6 4.5 4.5l1.4-1c.6-.5 3.6.5 3.6 1.5 0 1.5-1.6 2.5-3 2.5C10 18.5 5.5 14 5.5 9 5.5 7.6 6.5 6 8 6z" fill="#000"/></svg>
      123-456-1236
    </span>
  </div>
</section>

<section class="page page--back">
  <div class="brand">Marlo Kestrel<br><span style="font-size:7px">Photographer</span></div>

  <div class="back-content">
    <h2>HOW IT WORKS</h2>
    <ul class="checks">
      <li>We understand that your time is valuable, so let us handle the editing and delivery of your images. You shoot, and we take care of the rest.</li>
      <li>Images are edited and delivered within 1 working day</li>
    </ul>
    <h2>INCLUSIONS:</h2>
    <ul class="checks">
      <li>Full day face to face training (we come to you) and instructional handbook</li>
      <li>We will teach you everything you need to know about your equipment and how to take stunning real estate photographs</li>
      <li>Service turnaround within 1 working day</li>
      <li>Free HELP desk service Mon-Fri</li>
      <li>12 month Exclusivity (rural towns only) for a limited time</li>
    </ul>
    <h2>INVESTMENT</h2>
    <ul class="checks">
      <li>99 per listing for us to manage images including editing, quality control and delivery (10 Images)</li>
      <li>Ask us about competitive packages for photography equipment if required</li>
    </ul>
    <h2>SUMMARY</h2>
    <ul class="checks">
      <li>The KLD Real Estate Photography Editing and Support Service is the perfect solution for busy real estate professionals who want to take their business to the next level. Our service is affordable, flexible, and designed to help you showcase your listings in the best possible light.</li>
    </ul>
  </div>

  <div class="band"><h3>PHOTOGRAPHY SERVICES</h3></div>
  <div class="samples">
    <div class="sample" role="img" aria-label="Bright bedroom with large windows to the countryside" style="background:linear-gradient(160deg,#dcdcd8,#b8b2a6 50%,#f2f0ec)"></div>
    <div class="sample" role="img" aria-label="Stone and white farmhouse lit at twilight" style="background:linear-gradient(180deg,#6f7fa6,#b9a48a 50%,#d9d4cc)"></div>
    <div class="sample" role="img" aria-label="Black clifftop cabin above the ocean at sunset" style="background:linear-gradient(180deg,#9fb4cc,#e9c6b4 45%,#4e6f86 65%,#5d8a3e)"></div>
  </div>

  <div class="footer"><p>www.marlokestrel.com | info@marlokestrel.com</p></div>
  <div class="contact-pill">
    <span class="script">Contact Us Today</span>
    <span class="phone">
      <svg width="24" height="24" viewBox="0 0 24 24"><circle cx="12" cy="12" r="12" fill="#fff"/><path d="M8 6c1 0 2 3 1.5 3.6L8.5 11c.9 2 2.5 3.6 4.5 4.5l1.4-1c.6-.5 3.6.5 3.6 1.5 0 1.5-1.6 2.5-3 2.5C10 18.5 5.5 14 5.5 9 5.5 7.6 6.5 6 8 6z" fill="#000"/></svg>
      123-456-1236
    </span>
  </div>
</section>

</body>
</html>
```